Business Cards

We are an innovating group of real estate investors who buy beat up house's, fix them up, and resell them. We are in need of a business card that is catchy and stands out. We want it to say something like " Redbrick Property Group" Call us today

Industry/Entity Type

Business

Requirements
Must have
• Our logo which is updated

```html
<!DOCTYPE html>
<html lang="en">
<head>
<meta charset="utf-8">
<title>Business Card – Front and Back</title>
<link rel="stylesheet" href="https://fonts.googleapis.com/css2?family=Open+Sans:wght@400;600;700&display=swap">
<style>
  :root {
    --stage: #e9e6e1;
    --card-dark: #3b3b3d;
    --card-strip: #454547;
    --accent-green: #8cc63f;
    --accent-green-dark: #7ab232;
    --accent-purple: #8e3a9e;
    --stripe-light: #f2f2f2;
    --stripe-grey: #a9a9a9;
    --text-light: #ffffff;
    --text-soft: #e4e4e4;
  }
  * { box-sizing: border-box; margin: 0; padding: 0; }
  html, body { width: 1200px; height: 900px; overflow: hidden; }
  body {
    background: var(--stage);
    font-family: "Open Sans", Arial, sans-serif;
    display: flex;
    align-items: center;
    justify-content: center;
    gap: 50px;
  }
  .card {
    position: relative;
    width: 540px;
    height: 316px;
    background: var(--card-dark);
    overflow: hidden;
    box-shadow: 0 10px 24px rgba(0,0,0,0.35);
  }
  .card-stripes {
    position: absolute;
    left: 0; right: 0;
    top: 262px;
    height: 14px;
    background: linear-gradient(to bottom,
      var(--stripe-grey) 0 3px,
      var(--stripe-light) 3px 6px,
      var(--stripe-grey) 6px 9px,
      var(--stripe-light) 9px 12px,
      var(--stripe-grey) 12px 14px);
  }
  .card-band {
    position: absolute;
    left: 0; right: 0; bottom: 0;
    top: 276px;
    background: linear-gradient(to bottom, var(--accent-green), var(--accent-green-dark));
  }

  /* Front */
  .brand {
    position: absolute;
    left: 78px;
    top: 96px;
    display: flex;
    align-items: center;
    gap: 12px;
  }
  .brand-square {
    width: 42px; height: 42px;
    background: var(--accent-green);
  }
  .brand-text { display: flex; flex-direction: column; }
  .brand-name {
    font-size: 25px;
    font-weight: 600;
    color: var(--accent-purple);
    letter-spacing: -0.3px;
    line-height: 1.1;
  }
  .brand-tagline {
    font-size: 11px;
    color: var(--text-soft);
    margin-top: 2px;
  }
  .contact-strip {
    position: absolute;
    left: 0; right: 0;
    top: 192px;
    height: 70px;
    background: var(--card-strip);
    display: grid;
    grid-template-columns: 175px 160px 1fr;
    padding: 14px 0 0 36px;
  }
  .contact-col { display: flex; flex-direction: column; gap: 8px; }
  .contact-item {
    display: flex;
    align-items: center;
    gap: 6px;
    font-size: 10.5px;
    color: var(--text-soft);
  }
  .contact-item svg { width: 11px; height: 11px; flex: none; }

  /* Back */
  .back-content {
    position: absolute;
    left: 0; right: 0;
    top: 68px;
    display: flex;
    flex-direction: column;
    align-items: center;
  }
  .back-square {
    width: 44px; height: 44px;
    background: var(--accent-green);
    margin-bottom: 22px;
  }
  .back-headline {
    font-size: 26px;
    font-weight: 600;
    color: var(--text-light);
    letter-spacing: -0.3px;
  }
  .back-tagline {
    font-size: 22px;
    font-weight: 400;
    color: var(--text-light);
    letter-spacing: 2px;
    margin-top: 6px;
  }
</style>
</head>
<body>

<section class="card card-front">
  <div class="brand">
    <div class="brand-square"></div>
    <div class="brand-text">
      <span class="brand-name">Redbrick Property Group</span>
      <span class="brand-tagline">Call us today</span>
    </div>
  </div>

  <div class="contact-strip">
    <div class="contact-col">
      <span class="contact-item">
        <svg viewBox="0 0 12 12"><path d="M6 0.5a4 4 0 0 1 4 4c0 3-4 7-4 7s-4-4-4-7a4 4 0 0 1 4-4z" fill="#8cc63f"/><circle cx="6" cy="4.5" r="1.5" fill="#454547"/></svg>
        Address
      </span>
    </div>
    <div class="contact-col">
      <span class="contact-item">
        <svg viewBox="0 0 12 12"><path d="M3 1h2l1 3-1.5 1a6 6 0 0 0 2.5 2.5L8 6l3 1v2a1.5 1.5 0 0 1-1.5 1.5A8.5 8.5 0 0 1 1.5 2.5 1.5 1.5 0 0 1 3 1z" fill="#8cc63f"/></svg>
        Telephone
      </span>
      <span class="contact-item">
        <svg viewBox="0 0 12 12"><rect x="3" y="1" width="6" height="4" fill="#8cc63f"/><rect x="1" y="5" width="10" height="5" fill="#8cc63f"/><rect x="3" y="7" width="6" height="1" fill="#454547"/></svg>
        Fax
      </span>
    </div>
    <div class="contact-col">
      <span class="contact-item">
        <svg viewBox="0 0 12 12"><circle cx="6" cy="6" r="5" fill="#8cc63f"/><path d="M1 6h10M6 1c2 2 2 8 0 10M6 1c-2 2-2 8 0 10" stroke="#454547" stroke-width="0.8" fill="none"/></svg>
        www.yourwebsite.com
      </span>
      <span class="contact-item">
        <svg viewBox="0 0 12 12"><rect x="1" y="2.5" width="10" height="7" fill="none" stroke="#8cc63f" stroke-width="1.2"/><path d="M1 2.5l5 4 5-4" fill="none" stroke="#8cc63f" stroke-width="1.2"/></svg>
        your@email.com
      </span>
    </div>
  </div>

  <div class="card-stripes"></div>
  <div class="card-band"></div>
</section>

<section class="card card-back">
  <div class="back-content">
    <div class="back-square"></div>
    <h1 class="back-headline">REDBRICK PROPERTY GROUP</h1>
    <p class="back-tagline">CALL US TODAY</p>
  </div>
  <div class="card-stripes"></div>
  <div class="card-band"></div>
</section>

</body>
</html>
```